KPT Website

1. A fully functioning website
2. Should be either Linux, windows or Word Press based
3. Intend to have Lumrack host it
4. Photos should reflect diversity (gender/race)

```html
<!DOCTYPE html>
<html lang="en">
<head>
<meta charset="utf-8">
<title>KPT — Professional Consulting Agency</title>
<link href="https://fonts.googleapis.com/css2?family=Fira+Sans:wght@400;500;600;700&family=Open+Sans:wght@400;600;700&display=swap" rel="stylesheet">
<style>
:root{
  --red:#d71920;
  --red-dark:#a5121a;
  --ink:#222;
  --text:#555;
  --muted:#888;
  --line:#e5e5e5;
  --grey:#f4f4f4;
  --dark:#1c1c1c;
  --darker:#141414;
  --white:#fff;
}
*{box-sizing:border-box;margin:0;padding:0}
html,body{width:1200px;height:4945px;overflow:hidden}
body{font-family:"Open Sans",sans-serif;color:var(--text);background:var(--white);font-size:13px;line-height:1.6}
h1,h2,h3,h4,.heading{font-family:"Fira Sans",sans-serif;color:var(--ink);font-weight:500}
.wrap{width:720px;margin:0 auto;position:relative}
section,header,footer{position:relative;overflow:hidden}
.btn{display:inline-block;background:var(--red);color:var(--white);font-size:10px;font-weight:600;padding:6px 16px;border-radius:14px}
.kicker{color:var(--red);font-size:10px;text-align:center}
.sec-title{font-size:26px;text-align:center;margin-top:4px}
.bar{width:40px;height:2px;background:var(--red);margin:10px auto}
.bar.left{margin-left:0}
.lede{text-align:center;font-size:11px;color:var(--muted);width:380px;margin:6px auto 0;line-height:1.6}
.photo{display:block}

/* top */
.topbar{height:26px;background:var(--darker);color:#ccc;font-size:9px}
.topbar .wrap{display:flex;height:26px;align-items:center;gap:18px;width:1000px}
.topbar .dots{margin-left:auto;display:flex;gap:10px}
.topbar .dots span{width:8px;height:8px;border-radius:50%;background:#888}
.nav{height:64px;background:var(--white);border-bottom:1px solid var(--line)}
.nav .wrap{width:1000px;display:flex;align-items:center;height:64px}
.brand{display:flex;align-items:center;gap:8px;font-family:"Fira Sans",sans-serif;font-weight:700;color:var(--red);font-size:20px}
.brand i{width:22px;height:22px;border-radius:50%;background:var(--red);display:block}
.menu{margin-left:auto;display:flex;gap:26px;font-size:10px;font-weight:600;color:var(--ink)}
.menu .on{color:var(--red);border-bottom:2px solid var(--red);padding-bottom:3px}

/* hero */
.hero{height:530px}
.hero .photo{position:absolute;inset:0;background:linear-gradient(120deg,#9e0f15 0%,#c81a22 45%,#7a0a0f 100%)}
.hero h1{position:absolute;left:220px;top:148px;color:rgba(255,255,255,.55);font-size:30px;line-height:1.35;font-weight:600}
.hero .pager{position:absolute;bottom:10px;left:50%;transform:translateX(-50%);display:flex;gap:5px}
.hero .pager span{width:6px;height:6px;border-radius:50%;background:rgba(255,255,255,.7)}

/* features */
.features{height:430px;padding-top:60px}
.steps{display:flex;justify-content:space-between;margin-top:40px}
.step{width:150px;text-align:center}
.step .num{font-family:"Fira Sans",sans-serif;font-size:34px;font-weight:300;color:var(--ink)}
.step .dot{width:10px;height:10px;border:2px solid var(--red);border-radius:50%;margin:4px auto 8px}
.step h4{font-size:13px;font-weight:500}
.step p{font-size:10px;color:var(--muted);margin-top:6px;line-height:1.5}

/* welcome */
.welcome{height:350px;background:var(--grey)}
.welcome .wrap{display:flex;justify-content:space-between;align-items:center;height:350px}
.welcome .copy{width:330px}
.welcome h2{font-size:20px}
.welcome p{font-size:10px;color:var(--muted)}
.welcome ul{list-style:none;margin:10px 0 14px;font-size:10px;color:var(--ink)}
.welcome li::before{content:"";display:inline-block;width:5px;height:5px;background:var(--red);border-radius:50%;margin-right:6px;vertical-align:middle}
.welcome .photo{width:350px;height:230px;border-radius:4px;background:linear-gradient(135deg,#c9c2b8,#e7e1d6 50%,#9aa4ad)}

/* services */
.services{height:570px;padding-top:50px}
.cards{display:flex;justify-content:space-between;margin-top:40px}
.card{width:232px;background:var(--white);box-shadow:0 2px 12px rgba(0,0,0,.1)}
.card .photo{height:155px;background:linear-gradient(160deg,#b9c3cc,#e5e8eb 50%,#6f7c88)}
.card .body{padding:14px 16px 16px}
.card h4{font-size:12px}
.card h4::before{content:"";display:inline-block;width:5px;height:5px;background:var(--red);border-radius:50%;margin-right:6px;vertical-align:middle}
.card p{font-size:10px;color:var(--muted);margin:6px 0 12px;line-height:1.5}
.card .dark{display:block;background:var(--ink);color:#fff;text-align:center;font-size:9px;font-weight:600;padding:7px 0;border-radius:3px}

/* banner */
.banner{height:285px;color:#fff;text-align:center}
.banner .photo{position:absolute;inset:0;background:linear-gradient(100deg,#2b2b2b,#4a4a4a 50%,#1f1f1f)}
.banner .inner{position:relative;padding-top:78px}
.banner h2{color:#fff;font-size:28px;font-weight:600}
.banner h3{color:#fff;font-size:17px;margin:8px 0 16px}

/* partners */
.partners{height:110px;background:var(--white)}
.partners .wrap{display:flex;justify-content:space-between;align-items:center;height:110px;width:680px}
.badge{width:56px;height:40px;border-radius:6px;background:#2a2a2a}
.badge.round{border-radius:50%;width:44px;height:44px}

/* world */
.world{height:275px}
.world .wrap{display:flex;align-items:center;height:275px;gap:60px}
.world .photo{width:340px;height:190px;background:radial-gradient(ellipse at center,#e3e3e3 0%,#f2f2f2 60%,#fff 100%)}
.world .copy{width:300px}
.world h2{font-size:17px}
.world p{font-size:10px;color:var(--muted);margin:4px 0 14px}

/* testimonial */
.testimonial{background:linear-gradient(180deg,#ececec,#e2e2e2);text-align:center}
.testimonial.t1{height:390px;padding-top:50px}
.testimonial.t2{height:310px;padding-top:30px}
.quote-mark{color:var(--red);font-family:"Fira Sans",sans-serif;font-size:30px;line-height:1;margin-top:22px}
.quote{width:720px;margin:6px auto 0;font-size:11px;font-style:italic;color:var(--ink);line-height:1.7}
.who{font-family:"Fira Sans",sans-serif;color:var(--ink);font-weight:600;font-size:12px;margin-top:16px}
.role{font-size:9px;color:var(--muted)}
.arrows{display:flex;gap:6px;justify-content:center;margin-top:18px}
.arrows span{width:26px;height:26px;background:#fff;border-radius:3px;display:flex;align-items:center;justify-content:center}

.plans{height:170px;padding-top:78px}
.plans.p2{height:145px;padding-top:58px}

/* newsletter */
.news{height:120px;background:linear-gradient(100deg,#2a2a2a,#3a3a3a 50%,#222);color:#fff;text-align:center;padding-top:20px}
.news p{font-size:10px;width:420px;margin:0 auto;font-weight:600}
.news form{display:flex;justify-content:center;gap:8px;margin-top:16px}
.news .field{width:180px;height:28px;border-radius:14px;background:#fff;color:#999;font-size:9px;text-align:left;padding:7px 14px}
.news .btn{padding:8px 16px}

/* mission */
.mission{height:285px}
.mission .wrap{display:flex;justify-content:space-between;padding-top:50px}
.mission .copy{width:340px}
.mission .kick{color:var(--red);font-size:9px}
.mission h2{font-size:22px;line-height:1.3;margin-top:4px;font-weight:600}
.mission p{font-size:10px;color:var(--muted);line-height:1.6}
.mission ul{list-style:none;width:330px;margin-top:10px}
.mission li{font-size:10px;color:var(--ink);padding:10px 0;border-bottom:1px solid var(--line)}

/* cases */
.cases{height:510px;background:var(--grey);padding-top:50px}
.cases h2{font-size:18px}
.case-grid{display:grid;grid-template-columns:1fr 1fr;gap:24px 28px;margin-top:24px}
.case{background:#fff;display:flex;height:140px;box-shadow:0 2px 8px rgba(0,0,0,.06)}
.case .photo{width:175px;height:140px;background:linear-gradient(135deg,#a9b1b8,#dedad3 55%,#7d868e)}
.case .body{padding:14px 14px}
.case h4{font-size:12px;font-weight:600}
.case p{font-size:9px;color:var(--muted);margin:8px 0;line-height:1.5}
.case a{font-size:9px;color:var(--red);font-weight:600}

/* cta */
.cta{height:85px}
.cta .wrap{display:flex;align-items:center;justify-content:space-between;height:85px}
.cta h3{font-size:13px;font-weight:600}

/* footer */
.footer{height:290px;background:var(--darker);color:#aaa;font-size:9px}
.footer .cols{display:flex;justify-content:space-between;padding-top:30px}
.footer h4{color:#fff;font-size:13px;font-weight:600;margin-bottom:14px}
.footer .about{width:220px}
.footer .brand{font-size:18px;margin-bottom:10px}
.footer .brand i{width:18px;height:18px}
.footer .social{display:flex;gap:6px;margin-top:10px}
.footer .social span{width:16px;height:16px;border-radius:50%;background:#444}
.footer ul{list-style:none}
.footer .links li{margin-bottom:4px}
.footer .links li::before{content:"›";color:var(--red);margin-right:5px}
.footer .posts li{display:flex;gap:8px;margin-bottom:8px;width:150px}
.footer .posts .photo{width:34px;height:28px;background:linear-gradient(135deg,#666,#999);flex:none}
.footer .posts b{display:block;color:#ddd;font-weight:600}
.footer .tags{display:flex;flex-wrap:wrap;gap:5px;width:130px}
.footer .tags span{border:1px solid #444;padding:2px 7px;color:#ccc}
.footer .legal{position:absolute;bottom:0;left:0;right:0;border-top:1px solid #2a2a2a;padding:8px 0}
.footer .legal em{color:var(--red);font-style:normal}
</style>
</head>
<body>

<header class="topbar">
  <div class="wrap">
    <span>Welcome to Professional Consulting Agency</span>
    <span>(555) 014-2290</span>
    <span>hello@kpt-consult.com</span>
    <div class="dots"><span></span><span></span><span></span><span></span><span></span></div>
  </div>
</header>

<nav class="nav">
  <div class="wrap">
    <div class="brand"><i></i>KPT</div>
    <div class="menu">
      <span class="on">HOME</span><span>ABOUT</span><span>SERVICES</span><span>PROJECTS</span><span>DEALS</span><span>BLOG</span><span>PAGES</span><span>ELEMENTS</span><span>CONTACT</span>
      <svg width="12" height="12" viewBox="0 0 12 12"><circle cx="5" cy="5" r="3.5" fill="none" stroke="#222" stroke-width="1.5"/><line x1="7.5" y1="7.5" x2="11" y2="11" stroke="#222" stroke-width="1.5"/></svg>
    </div>
  </div>
</nav>

<section class="hero">
  <div class="photo" role="img" aria-label="Business professional at work, tinted red"></div>
  <h1>We will help to improve<br>your business</h1>
  <div class="pager"><span></span><span></span><span></span></div>
</section>

<section class="features">
  <div class="wrap">
    <p class="kicker">What we offer</p>
    <h2 class="sec-title">Make Successful Business</h2>
    <div class="bar"></div>
    <p class="lede">We guide growing teams through strategy, planning and change so every decision moves the business forward.</p>
    <div class="steps">
      <div class="step"><div class="num">01</div><div class="dot"></div><h4>Professional Consulting</h4><p>Clear advice from experienced advisors who know your market well.</p></div>
      <div class="step"><div class="num">02</div><div class="dot"></div><h4>Online Reputation</h4><p>Build trust online and keep your brand story strong and consistent.</p></div>
      <div class="step"><div class="num">03</div><div class="dot"></div><h4>Market Research</h4><p>Insight into customers and rivals to shape smarter growth plans.</p></div>
      <div class="step"><div class="num">04</div><div class="dot"></div><h4>Budget Friendly</h4><p>Flexible packages that fit small teams and large firms alike.</p></div>
    </div>
  </div>
</section>

<section class="welcome">
  <div class="wrap">
    <div class="copy">
      <h2>Welcome To Our Consulting Agency</h2>
      <div class="bar left"></div>
      <p>We partner with leaders to solve hard problems, improve performance and grow with confidence. Our diverse team brings fresh ideas and proven methods to every project we take on.</p>
      <ul>
        <li>Integration consultant, information technology consulting</li>
        <li>Compliance, financial, market consultant</li>
        <li>Employment consultant, environmental consultant</li>
      </ul>
      <span class="btn">Read More</span>
    </div>
    <div class="photo" role="img" aria-label="Diverse team of colleagues reviewing work on a tablet in an office"></div>
  </div>
</section>

<section class="services">
  <div class="wrap">
    <p class="kicker">What we offer</p>
    <h2 class="sec-title">We Provide All Kind Of Business Services</h2>
    <div class="bar"></div>
    <p class="lede">From first plan to final launch, our advisors support each stage of your company's journey.</p>
    <div class="cards">
      <div class="card"><div class="photo" role="img" aria-label="Smiling businesswoman with her team"></div><div class="body"><h4>Professional Advisor</h4><p>Trusted guidance on strategy, operations and growth for your team.</p><span class="dark">Learn More</span></div></div>
      <div class="card"><div class="photo" role="img" aria-label="Businessman in a suit in a glass office"></div><div class="body"><h4>Financial Services Consulting</h4><p>Sound planning for budgets, funding and long term financial health.</p><span class="dark">Learn More</span></div></div>
      <div class="card"><div class="photo" role="img" aria-label="Businesswoman standing in front of colleagues"></div><div class="body"><h4>Consumer Product Consulting</h4><p>Shape products customers love, from research through to launch.</p><span class="dark">Learn More</span></div></div>
    </div>
  </div>
</section>

<section class="banner">
  <div class="photo" role="img" aria-label="Team meeting in a dim office"></div>
  <div class="inner">
    <h2>Doing the right thing</h2>
    <h3>At the Right Time.</h3>
    <span class="btn">Become a Client</span>
  </div>
</section>

<section class="partners">
  <div class="wrap">
    <div class="badge round"></div><div class="badge"></div><div class="badge round"></div><div class="badge"></div><div class="badge"></div><div class="badge round"></div>
  </div>
</section>

<section class="world">
  <div class="wrap">
    <div class="photo" role="img" aria-label="World map with office locations"></div>
    <div class="copy">
      <h2>We are Available Worldwide</h2>
      <div class="bar left"></div>
      <p>Our offices and partners span several continents, so help is always close by. Wherever you operate, our team can meet you there and support your plans.</p>
      <span class="btn">Contact Us</span>
    </div>
  </div>
</section>

<section class="testimonial t1">
  <p class="kicker">Testimonials</p>
  <h2 class="sec-title">What People Say</h2>
  <div class="bar"></div>
  <div class="quote-mark">&ldquo;</div>
  <p class="quote">Working with this team changed how we plan and decide. They listened closely, challenged our thinking and gave us a clear road map. Within a year our results had grown and our staff felt more confident about the future.</p>
  <p class="who">Jalen Norby</p>
  <p class="role">Marketing Lead</p>
  <div class="arrows">
    <span><svg width="8" height="8" viewBox="0 0 8 8"><path d="M5.5 1 2.5 4l3 3" fill="none" stroke="#222" stroke-width="1.3"/></svg></span>
    <span><svg width="8" height="8" viewBox="0 0 8 8"><path d="M2.5 1 5.5 4l-3 3" fill="none" stroke="#222" stroke-width="1.3"/></svg></span>
  </div>
</section>

<section class="plans">
  <p class="kicker">Our Packages</p>
  <h2 class="sec-title">Pick The Best Plan For You</h2>
  <div class="bar"></div>
  <p class="lede">Choose a package that fits your goals and budget today.</p>
</section>

<section class="testimonial t2">
  <div class="quote-mark">&ldquo;</div>
  <p class="quote">Working with this team changed how we plan and decide. They listened closely, challenged our thinking and gave us a clear road map. Within a year our results had grown and our staff felt more confident about the future.</p>
  <p class="who">Jalen Norby</p>
  <p class="role">Marketing Lead</p>
  <div class="arrows">
    <span><svg width="8" height="8" viewBox="0 0 8 8"><path d="M5.5 1 2.5 4l3 3" fill="none" stroke="#222" stroke-width="1.3"/></svg></span>
    <span><svg width="8" height="8" viewBox="0 0 8 8"><path d="M2.5 1 5.5 4l-3 3" fill="none" stroke="#222" stroke-width="1.3"/></svg></span>
  </div>
</section>

<section class="plans p2">
  <p class="kicker">Our Packages</p>
  <h2 class="sec-title">Pick The Best Plan For You</h2>
  <div class="bar"></div>
</section>

<section class="news">
  <p>Join our mailing list for practical tips, case studies and news from our consulting team every month.</p>
  <form>
    <div class="field">Enter Your Email Address</div>
    <span class="btn">Subscribe</span>
  </form>
</section>

<section class="mission">
  <div class="wrap">
    <div class="copy">
      <p class="kick">Our mission</p>
      <h2>Our Mission is to Turn Your Ideas Into Businesses.</h2>
      <div class="bar left"></div>
      <p>We help founders and leaders turn bold ideas into steady, lasting companies through honest advice, careful planning and hands-on support at every step of the way.</p>
    </div>
    <ul>
      <li>Market Research</li>
      <li>Sales Services</li>
      <li>Online Reputation</li>
      <li>Strategic Consulting</li>
    </ul>
  </div>
</section>

<section class="cases">
  <div class="wrap">
    <h2>Featured Cases</h2>
    <div class="bar left"></div>
    <div class="case-grid">
      <div class="case"><div class="photo" role="img" aria-label="Colleagues discussing a project at a table"></div><div class="body"><h4>Social Media Marketing</h4><p>A fresh social plan that doubled reach for a retail client.</p><a>Learn More</a></div></div>
      <div class="case"><div class="photo" role="img" aria-label="Woman presenting to a small group"></div><div class="body"><h4>Sensitivity Analysis</h4><p>Risk modelling that guided a major investment choice.</p><a>Learn More</a></div></div>
      <div class="case"><div class="photo" role="img" aria-label="Team working together on laptops"></div><div class="body"><h4>Project Governance</h4><p>Clear structure that kept a large rollout on schedule.</p><a>Learn More</a></div></div>
      <div class="case"><div class="photo" role="img" aria-label="Two colleagues reviewing documents"></div><div class="body"><h4>Market Assessment</h4><p>Research that opened a new regional market for growth.</p><a>Learn More</a></div></div>
    </div>
  </div>
</section>

<section class="cta">
  <div class="wrap">
    <h3>Looking for Professional Approach and Quality Services ?</h3>
    <span class="btn">Contact Us</span>
  </div>
</section>

<footer class="footer">
  <div class="wrap">
    <div class="cols">
      <div class="about">
        <h4>About Us</h4>
        <div class="brand"><i></i>KPT</div>
        <p>We are a consulting agency helping teams plan, grow and lead with confidence in a changing world.</p>
        <div class="social"><span></span><span></span><span></span><span></span><span></span></div>
      </div>
      <div>
        <h4>Quick Links</h4>
        <ul class="links"><li>Strategic Consulting</li><li>Sales Services</li><li>Market Research</li><li>Online Reputation</li><li>Strategic Consulting</li><li>Sales Services</li><li>Market Research</li></ul>
      </div>
      <div>
        <h4>Recent Posts</h4>
        <ul class="posts">
          <li><div class="photo" role="img" aria-label="Post thumbnail"></div><div><b>April 20, 2024</b>How we build better teams</div></li>
          <li><div class="photo" role="img" aria-label="Post thumbnail"></div><div><b>April 18, 2024</b>Effective solutions today</div></li>
          <li><div class="photo" role="img" aria-label="Post thumbnail"></div><div><b>April 12, 2024</b>Steps for steady growth</div></li>
        </ul>
      </div>
      <div>
        <h4>Tags</h4>
        <div class="tags"><span>Art</span><span>Business</span><span>Cards</span><span>Consultant</span><span>Creative</span><span>Events</span><span>Idea</span><span>Lite</span><span>Mail</span><span>Web Design</span></div>
      </div>
    </div>
  </div>
  <div class="legal"><div class="wrap"><em>KPT</em> © 2024. All rights reserved.</div></div>
</footer>

</body>
</html>
```